Bref créative
The Lanternwrights
We get IT done right!
Professional
Rosalind Kettering
Partner
48 Thornapple Lane
Marlow Heights, PA 19533
rosalind.k.kettering@thelanternwrights.net
www.thelanternwrights.net
logo will be attached
second set of business cards needed
Dean Oltveld
dean.oltveld@thelanternwrights.net
Your Trusted Advisors
Updated logo in CMYK format

```html
<!DOCTYPE html>
<html lang="en">
<head>
<meta charset="utf-8">
<title>The Lanternwrights — Business Card</title>
<link href="https://fonts.googleapis.com/css2?family=Open+Sans:wght@400;600;800&display=swap" rel="stylesheet">
<style>
  :root {
    --orange: #f04a0f;
    --orange-light: #ff7a2a;
    --red: #d9240c;
    --blue: #1b5fb0;
    --ink: #1e1e1e;
    --paper: #ffffff;
    --stage: #ffffff;
  }
  * { box-sizing: border-box; margin: 0; padding: 0; }
  html, body { width: 1200px; height: 535px; overflow: hidden; background: var(--stage); }
  body { font-family: "Open Sans", Arial, sans-serif; color: var(--ink); position: relative; }

  .card {
    position: absolute; top: 98px; width: 550px; height: 340px;
    border-radius: 22px; overflow: hidden;
    box-shadow: 0 4px 14px rgba(0,0,0,0.18);
  }
  .card-front { left: 30px; background: var(--paper); }
  .card-back {
    left: 620px;
    background: radial-gradient(circle at 50% 45%, var(--orange-light) 0%, var(--orange) 55%, var(--red) 100%);
  }

  .band { position: absolute; left: 0; width: 100%; }
  .band svg { display: block; width: 100%; height: 100%; }
  .band-top { top: 0; height: 26px; }
  .band-bottom { bottom: 0; height: 30px; }

  .brand { position: absolute; text-align: center; }
  .brand-mark { display: block; margin: 0 auto; border-radius: 50%; }
  .brand-name { font-weight: 800; letter-spacing: -0.5px; line-height: 1; white-space: nowrap; }

  .card-front .brand { left: 30px; top: 58px; width: 310px; }
  .card-front .brand-mark { width: 84px; height: 84px; margin-bottom: 12px; background: var(--orange); }
  .card-front .brand-name { font-size: 26px; color: var(--ink); }

  .card-back .brand { left: 0; top: 100px; width: 100%; }
  .card-back .brand-mark { width: 86px; height: 86px; margin-bottom: 14px; background: #fff1ea; }
  .card-back .brand-name { font-size: 30px; color: #2a2a2a; }

  .contact { position: absolute; left: 26px; top: 236px; font-size: 12.5px; line-height: 1.65; white-space: nowrap; }
  .contact .label { color: var(--red); font-weight: 800; display: inline-block; width: 16px; }

  .person { position: absolute; left: 360px; top: 234px; width: 170px; }
  .person-name { color: var(--orange); font-weight: 600; font-size: 16px; white-space: nowrap; }
  .person-role { font-size: 12.5px; margin-top: 2px; }

  .website {
    position: absolute; right: 28px; bottom: 6px;
    color: #ffffff; font-size: 14px; font-weight: 400;
  }
</style>
</head>
<body>

<section class="card card-front" aria-label="Business card front">
  <div class="band band-top">
    <svg viewBox="0 0 550 26" preserveAspectRatio="none">
      <rect x="0" y="0" width="550" height="10" fill="var(--red)"/>
      <polygon points="0,10 550,10 550,14 0,14" fill="var(--orange)"/>
      <polygon points="420,0 440,0 456,26 436,26" fill="var(--blue)"/>
      <polygon points="446,0 460,0 476,26 462,26" fill="var(--paper)"/>
      <polygon points="460,0 550,0 550,26 476,26" fill="var(--orange)"/>
    </svg>
  </div>

  <div class="brand">
    <span class="brand-mark"></span>
    <div class="brand-name">THE LANTERNWRIGHTS</div>
  </div>

  <div class="contact">
    <div>48 Thornapple Lane Marlow Heights, PA 19533</div>
    <div><span class="label">E</span>: rosalind.k.kettering@thelanternwrights.net</div>
    <div><span class="label">C</span>: 484-555-0148</div>
  </div>

  <div class="person">
    <div class="person-name">Rosalind Kettering</div>
    <div class="person-role">Partner</div>
  </div>

  <div class="band band-bottom">
    <svg viewBox="0 0 550 30" preserveAspectRatio="none">
      <rect x="0" y="0" width="550" height="30" fill="var(--orange)"/>
      <rect x="0" y="0" width="550" height="4" fill="var(--red)"/>
      <polygon points="300,30 318,0 330,0 312,30" fill="var(--paper)"/>
      <polygon points="312,30 330,0 344,0 326,30" fill="var(--blue)"/>
    </svg>
  </div>
  <div class="website">www.thelanternwrights.net</div>
</section>

<section class="card card-back" aria-label="Business card back">
  <div class="brand">
    <span class="brand-mark"></span>
    <div class="brand-name">THE LANTERNWRIGHTS</div>
  </div>
</section>

</body>
</html>
```